Quiet Verses Across Winter Evenings

Need a BOOK COVER, SPINE, and BACK for above named book. This is the story of my late wife (a university professor) told through her own songs and poems. It is about the people she loved, especially her grand children, her extensive professional and life interests, her family, friends, and festivities, her illness, etc.
Updates

Need extra days to review

Target Market(s)

Family and friends

Font styles to use
Other font styles liked:
• Times New Roman

Requirements
Must have
• Regret I haven't given much thought to it...
Nice to have
• Regret I haven't given much thought to it..
Should not have

```html
<!DOCTYPE html>
<html lang="en">
<head>
<meta charset="utf-8">
<title>Quiet Verses Across Winter Evenings – Book Cover</title>
<link href="https://fonts.googleapis.com/css2?family=Quicksand:wght@300;400&family=Ubuntu:wght@700&display=swap" rel="stylesheet">
<style>
  :root {
    --page-bg: #f1f1f2;
    --cover-dark: #07080b;
    --streak-teal: #2c5a5e;
    --streak-grey: #5d6570;
    --back-lavender: #c9c4e4;
    --back-mid: #8e8ba6;
    --title-blue: #8f9bd8;
    --subtitle-white: #f2f4f6;
    --body-navy: #1c1d3a;
    --art-violet: #9b5ea8;
    --art-pale: #dfe9ea;
    --art-teal: #3f8c92;
  }
  * { margin: 0; padding: 0; box-sizing: border-box; }
  html, body {
    width: 1200px; height: 1000px; overflow: hidden;
    background: var(--page-bg);
  }
  .canvas {
    position: relative; width: 1200px; height: 1000px;
  }
  .cover {
    position: absolute; top: 180px; width: 420px; height: 640px;
    overflow: hidden;
    box-shadow: 0 20px 40px rgba(0,0,0,0.18);
  }
  /* Back cover */
  .back-cover {
    left: 150px;
    background: linear-gradient(180deg, #0c0d12 0%, #3b3a48 30%, var(--back-mid) 55%, var(--back-lavender) 100%);
  }
  .back-streaks {
    position: absolute; inset: 0;
    background: linear-gradient(170deg, transparent 28%, rgba(220,220,235,0.35) 34%, transparent 40%, transparent 55%, rgba(255,255,255,0.25) 60%, transparent 66%);
  }
  .back-title {
    position: absolute; left: 36px; top: 36px;
    font-family: "Quicksand", sans-serif; font-weight: 300;
    color: var(--title-blue); font-size: 27px; line-height: 1.1;
  }
  .back-title .sub { display: block; color: var(--subtitle-white); font-size: 19px; }
  .back-blurb {
    position: absolute; left: 34px; right: 34px; top: 190px;
    font-family: "Ubuntu", sans-serif; font-weight: 700;
    font-size: 12px; line-height: 1.4; color: var(--body-navy);
    text-align: center;
  }
  .back-blurb p { margin-bottom: 24px; }
  /* Front cover */
  .front-cover {
    left: 630px;
    background: var(--cover-dark);
  }
  .front-streaks {
    position: absolute; inset: 0;
    background:
      linear-gradient(160deg, transparent 14%, rgba(93,101,112,0.55) 22%, transparent 30%),
      linear-gradient(165deg, transparent 32%, rgba(44,90,94,0.6) 40%, transparent 48%),
      linear-gradient(175deg, transparent 70%, rgba(44,90,94,0.7) 90%);
  }
  .front-title {
    position: absolute; left: 34px; top: 26px;
    font-family: "Quicksand", sans-serif; font-weight: 300;
    color: var(--title-blue); line-height: 0.95;
  }
  .front-title .line-a { display: block; font-size: 64px; }
  .front-title .line-b { display: block; font-size: 64px; padding-left: 60px; }
  .front-subtitle {
    position: absolute; left: 70px; top: 200px;
    font-family: "Quicksand", sans-serif; font-weight: 300;
    color: var(--subtitle-white); line-height: 1.1;
  }
  .front-subtitle .small { display: block; font-size: 26px; }
  .front-subtitle .large { display: block; font-size: 30px; }
  .cover-art {
    position: absolute; left: 50px; top: 300px; width: 310px; height: 260px;
    border-radius: 30% 40% 45% 35%;
    background: radial-gradient(circle at 45% 30%, var(--art-violet) 0%, rgba(155,94,168,0.4) 20%, var(--art-pale) 45%, var(--art-teal) 80%, rgba(63,140,146,0) 100%);
  }
  .author {
    position: absolute; left: 0; right: 0; bottom: 38px; text-align: center;
    font-family: "Quicksand", sans-serif; font-weight: 400;
    color: var(--subtitle-white); font-size: 19px; letter-spacing: 0.5px;
  }
</style>
</head>
<body>
<main class="canvas">
  <section class="cover back-cover">
    <div class="back-streaks"></div>
    <h2 class="back-title">Quiet Verses <span class="sub">Across Winter Evenings</span></h2>
    <div class="back-blurb">
      <p>These songs and poems were written over many years, at kitchen tables, in lecture halls and on long train rides home after a day of teaching.</p>
      <p>They speak of grandchildren learning to walk, of festivals lit with lamps, of friends who stayed for dinner and of the quiet joy of ordinary days.</p>
      <p>They also speak of illness, patience and courage, written with the same warmth and curiosity she brought to every student and every class she taught.</p>
      <p>Gathered here by her family, these pages keep her voice close, so that those who loved her can hear it again, one verse at a time.</p>
      <p>For her grandchildren, her friends and all who shared her table, with love.</p>
    </div>
  </section>

  <section class="cover front-cover">
    <div class="front-streaks"></div>
    <h1 class="front-title">
      <span class="line-a">Quiet</span>
      <span class="line-b">Verses</span>
    </h1>
    <p class="front-subtitle">
      <span class="small">across</span>
      <span class="large">Winter Evenings</span>
    </p>
    <div class="cover-art" role="img" aria-label="Illustration of a pale open-hand shape holding a bird's nest with blue eggs, purple thistle and green daisy blossoms, over teal branching light"></div>
    <p class="author">Meera Kulkarni Rao</p>
  </section>
</main>
</body>
</html>
```